Lena Corvell Business Card

I need a business card that reflects my current website: itslenacorvell.example and screenshot attached. If we keep the color scheme of the site and sample card below that would be ideal. The business card should include the information on the attached sample cards.

Industry/Entity Type

Business

```html
<!DOCTYPE html>
<html lang="en">
<head>
<meta charset="utf-8">
<title>Lena Corvell Business Card</title>
<link href="https://fonts.googleapis.com/css2?family=Didact+Gothic&display=swap" rel="stylesheet">
<style>
  :root {
    --teal: #5ab5a3;
    --teal-text: #5cbfae;
    --ink: #3a3a3a;
    --paper: #ffffff;
    --backdrop: #ecebe8;
  }
  * { margin: 0; padding: 0; box-sizing: border-box; }
  html, body {
    width: 1200px;
    height: 900px;
    overflow: hidden;
    background: var(--backdrop);
    font-family: "Didact Gothic", "Century Gothic", sans-serif;
  }
  .sheet {
    width: 1200px;
    height: 900px;
    display: flex;
    flex-direction: column;
    align-items: center;
    justify-content: center;
    gap: 48px;
  }
  .card {
    width: 660px;
    height: 377px;
    position: relative;
    box-shadow: 0 6px 18px rgba(0, 0, 0, 0.12);
  }
  .card-front {
    background: var(--teal);
    display: flex;
    align-items: center;
    justify-content: center;
  }
  .front-name {
    color: var(--paper);
    font-size: 40px;
    letter-spacing: 1px;
    margin-top: -30px;
  }
  .card-back {
    background: var(--paper);
  }
  .details {
    position: absolute;
    left: 150px;
    top: 112px;
  }
  .back-name {
    color: var(--teal-text);
    font-size: 34px;
    margin-left: 70px;
    letter-spacing: 0.5px;
  }
  .roles {
    color: var(--teal-text);
    font-size: 11.5px;
    margin-top: 6px;
    letter-spacing: 0.2px;
  }
  .contact {
    list-style: none;
    margin-top: 18px;
    color: var(--ink);
    font-size: 12.5px;
    line-height: 1.55;
  }
</style>
</head>
<body>
  <main class="sheet">
    <section class="card card-front" aria-label="Card front">
      <h1 class="front-name">Lena Corvell</h1>
    </section>

    <section class="card card-back" aria-label="Card back">
      <div class="details">
        <h2 class="back-name">Lena Corvell</h2>
        <p class="roles">Brand Curator | Digital Storyteller | Social Entrepreneur</p>
        <ul class="contact">
          <li>me@lenacorvell.example</li>
          <li>210.555.0147</li>
          <li>[fb] [t] [ig] @itslenacorvell</li>
          <li>www.itslenacorvell.example</li>
        </ul>
      </div>
    </section>
  </main>
</body>
</html>
```